VeroTide Powerpoint design

We've recently redesigned our logos and would like a single presentation format that we can easily interchange the logos attached into. The presentation will be used for general company sales information. The group is called VeroTide and has 2 companies, k7gridworks and Quiet Harbor. We're an IT services company who specialises in Broadband and general network services.

Target Market(s)

Professional

```html
<!DOCTYPE html>
<html lang="en">
<head>
<meta charset="utf-8">
<title>VeroTide Group – Presentation</title>
<link href="https://fonts.googleapis.com/css2?family=Montserrat:wght@500;600;700&family=Roboto:wght@400;500;700&display=swap" rel="stylesheet">
<style>
:root{
  --page:#e4e4e4;
  --white:#ffffff;
  --green-dark:#006b3a;
  --green-light:#8dc63f;
  --blue:#29a6de;
  --red:#d0112b;
  --ink:#111111;
  --grey:#6b6b6b;
  --logo-ink:#3a3a3a;
  --track:#ffffff;
}
*{margin:0;padding:0;box-sizing:border-box}
html,body{width:1200px;height:3976px;overflow:hidden;background:var(--page)}
body{position:relative;font-family:"Roboto",Arial,sans-serif;color:var(--ink)}
.slide{position:absolute;left:91px;width:1017px;height:571px;background:var(--white);overflow:hidden}
.s1{top:105px}.s2{top:744px}.s3{top:1383px}.s4{top:2022px}.s5{top:2661px}.s6{top:3300px}
.backdrop{position:absolute;inset:0}
.s1 .backdrop{background:linear-gradient(110deg,#ffffff 0%,#f4f6f5 45%,#e9eceb 100%)}
.s4 .backdrop,.s5 .backdrop{background:linear-gradient(120deg,#f7f9fb 0%,#eef2f6 60%,#e6ecf2 100%)}
.s6 .backdrop{background:linear-gradient(180deg,#f5f6f6 0%,#ffffff 60%,#f2f3f3 100%)}

.brand{position:absolute;display:flex;align-items:center;gap:10px;font-family:"Montserrat",sans-serif;font-weight:600;color:var(--logo-ink)}
.brand .dot{border-radius:50%;background:var(--green-dark);flex:none}
.brand-top{left:711px;top:32px;font-size:44px}
.brand-top .dot{width:40px;height:40px}

.title-band{position:absolute;left:0;top:32px;width:570px;height:48px;background:var(--green-dark);border-radius:0 24px 24px 0;color:var(--white);font-family:"Montserrat",sans-serif;font-weight:600;font-size:27px;line-height:48px;padding-left:63px}

.partners{position:absolute;left:60px;top:508px;display:flex;gap:34px}
.partner{display:flex;align-items:center;gap:8px;font-family:"Montserrat",sans-serif;font-weight:500;font-size:31px;color:var(--logo-ink)}
.partner .dot{width:34px;height:34px;border-radius:50%;background:var(--blue)}
.partner.k7 .dot{background:var(--red)}
.page-no{position:absolute;right:0;top:503px;width:204px;height:48px;background:var(--green-light);border-radius:24px 0 0 24px;color:var(--white);font-weight:700;font-size:17px;line-height:48px;text-align:center}

/* slide 1 */
.s1 .brand{left:60px;top:36px;font-size:52px}
.s1 .brand .dot{width:48px;height:48px}
.welcome{position:absolute;left:62px;top:208px;font-family:"Montserrat",sans-serif;font-weight:600;font-size:28px}
.hero-title{position:absolute;left:56px;top:250px;font-family:"Montserrat",sans-serif;font-weight:700;font-size:64px;letter-spacing:.5px}
.hero-text{position:absolute;left:62px;top:348px;width:460px;font-size:14px;font-weight:700;line-height:27px}
.hero-art{position:absolute;left:590px;top:60px;width:390px;height:470px;border-radius:50%;background:radial-gradient(circle at 45% 45%,rgba(0,107,58,.16),rgba(41,166,222,.10) 55%,rgba(255,255,255,0) 72%)}

/* slide 2 */
.photo{position:absolute;border-radius:6px}
.about-frame{position:absolute;left:51px;top:143px;width:420px;height:320px;border-left:3px solid var(--blue);border-bottom:3px solid var(--blue)}
.about-frame::after{content:"";position:absolute;right:-3px;bottom:-3px;width:60px;height:14px;border-right:3px solid var(--red);border-bottom:3px solid var(--red)}
.about-photo{left:63px;top:128px;width:429px;height:326px;border-radius:0;background:linear-gradient(160deg,#0c1d3a 0%,#1c4f8a 45%,#7fb2dd 75%,#e8f1f8 100%)}
.about-text{position:absolute;left:538px;top:130px;width:420px;font-size:13.5px;line-height:25.5px;color:var(--grey);text-align:justify}
.about-text p+p{margin-top:8px}

/* slide 3 */
.service{position:absolute;top:140px;width:414px}
.service .photo{position:static;display:block;width:414px;height:258px;border-radius:10px}
.service h3{margin-top:18px;text-align:center;font-size:25px;font-weight:700}
.svc-a{left:79px}.svc-b{left:523px}
.svc-a .photo{background:linear-gradient(135deg,#e9dccb 0%,#b99a78 45%,#4e3b2c 100%)}
.svc-b .photo{background:linear-gradient(180deg,#1e3d63 0%,#3f6f9f 50%,#8fd3f0 100%)}

/* slide 4 */
.reason{position:absolute;width:290px}
.reason h4{font-size:18px;font-weight:700;margin-bottom:14px}
.reason p{font-size:14px;line-height:25.5px;color:var(--grey)}
.reason.left{left:53px;text-align:right}
.reason.right{left:672px}
.r1{top:130px}.r2{top:342px}.r3{top:136px}.r4{top:322px}
.wheel{position:absolute;left:356px;top:144px;width:306px;height:306px}

/* slide 5 */
.analysis-text{position:absolute;left:60px;top:163px;width:442px;font-size:14px;line-height:25.5px;color:var(--grey);text-align:justify}
.bars{position:absolute;left:540px;top:164px;width:412px;list-style:none}
.bars li{position:relative;height:30px;margin-bottom:17.7px;background:var(--track);border-radius:15px;box-shadow:0 1px 4px rgba(0,0,0,.15)}
.bars .fill{position:absolute;left:0;top:0;height:100%;border-radius:15px;background:var(--blue)}
.bars .red .fill{background:var(--red)}
.bars .pct{position:absolute;right:18px;top:0;line-height:30px;font-size:9px;font-weight:700;color:#333}

/* slide 6 */
.s6 .brand{left:380px;top:112px;font-size:50px}
.s6 .brand .dot{width:46px;height:46px}
.thanks{position:absolute;left:0;right:0;top:190px;text-align:center;font-family:"Montserrat",sans-serif;font-weight:700;font-size:96px}
.contact{position:absolute;top:353px;display:flex;gap:14px}
.contact .icon{width:48px;height:48px;border-radius:50%;background:var(--green-dark);display:flex;align-items:center;justify-content:center;flex:none}
.contact strong{display:block;font-size:17px;font-weight:700;margin-top:6px}
.contact span{display:block;font-size:14px;margin-top:4px}
.c1{left:87px}.c2{left:442px}.c3{left:727px}
</style>
</head>
<body>

<section class="slide s1">
  <div class="backdrop" role="img" aria-label="Faint office interior photo"></div>
  <div class="brand"><span class="dot"></span>VeroTide</div>
  <p class="welcome">Welcome To</p>
  <h1 class="hero-title">VeroTide Group</h1>
  <p class="hero-text">Lorem ipsum dolor sit amet consectetur adipiscing sed do eiusmod tempor incididunt ut labore et dolore magna aliquat aliquip ex ea commodo consequat.</p>
  <div class="hero-art" role="img" aria-label="Soft coloured network graphic"></div>
</section>

<section class="slide s2">
  <div class="title-band">About Us</div>
  <div class="brand brand-top"><span class="dot"></span>VeroTide</div>
  <div class="about-frame"></div>
  <div class="photo about-photo" role="img" aria-label="Satellite orbiting above the Earth"></div>
  <div class="about-text">
    <p>Lorem ipsum dolor sit amet, consectetur adipiscing elit, sed do eiusmod tempor incididunt ut labore et dolore magna aliqua. Ut enim ad minim veniam, quis nostrud exercitation ullamco laboris nisi ut aliquip ex ea commodo consequat. Duis aute irure dolor in reprehenderit in voluptate velit esse</p>
    <p>Sed ut perspiciatis unde omnis iste natus error sit voluptatem accusantium doloremque laudantium, totam rem aperiam, eaque ipsa quae ab illo inventore veritatis et quasi architecto beatae vitae dicta sunt explicabo. Nemo enim ipsam voluptatem quia voluptas sit aspernatur aut odit aut fugit, sed quia consequuntur magni dolores eos qui ratione voluptatem sequi nesciunt. Neque porro quisquam</p>
  </div>
  <div class="partners"><div class="partner"><span class="dot"></span>Quiet Harbor</div><div class="partner k7"><span class="dot"></span>k7gridworks</div></div>
  <div class="page-no">Page No:02</div>
</section>

<section class="slide s3">
  <div class="title-band">Our Services</div>
  <div class="brand brand-top"><span class="dot"></span>VeroTide</div>
  <div class="service svc-a"><div class="photo" role="img" aria-label="Person using a laptop beside a wireless router"></div><h3>Broadband</h3></div>
  <div class="service svc-b"><div class="photo" role="img" aria-label="Businessman overlooking a connected city skyline at night"></div><h3>General network services</h3></div>
  <div class="partners"><div class="partner"><span class="dot"></span>Quiet Harbor</div><div class="partner k7"><span class="dot"></span>k7gridworks</div></div>
  <div class="page-no">Page No:03</div>
</section>

<section class="slide s4">
  <div class="backdrop" role="img" aria-label="Faint technology background photo"></div>
  <div class="title-band">Why Choose Us</div>
  <div class="brand brand-top"><span class="dot"></span>VeroTide</div>
  <div class="reason left r1"><h4>Lorem ipsum dolor consectetur</h4><p>Lorem ipsum dolor consectetur &nbsp;sed do eiusmod tempor incididunt uti labore et magnad aliquat aveniamnostrud</p></div>
  <div class="reason left r2"><h4>Lorem ipsum dolor consectetur</h4><p>Lorem ipsum dolor consectetur &nbsp;sed do eiusmod tempor incididunt uti labore et magnad aliquat aveniamnostrud</p></div>
  <div class="reason right r3"><h4>Lorem ipsum dolor consectetur</h4><p>Lorem ipsum dolor consectetur &nbsp;sed do eiusmod tempor incididunt uti labore et magnad aliquat aveniamnostrud</p></div>
  <div class="reason right r4"><h4>Lorem ipsum dolor consectetur</h4><p>Lorem ipsum dolor consectetur &nbsp;sed do eiusmod tempor incididunt uti labore et magnad aliquat aveniamnostrud</p></div>
  <svg class="wheel" viewBox="0 0 306 306" aria-hidden="true">
    <path d="M150 0 A153 153 0 0 0 0 150 H78 A75 75 0 0 1 150 78 Z" fill="#006b3a"/>
    <path d="M156 0 A153 153 0 0 1 306 150 H228 A75 75 0 0 0 156 78 Z" fill="#29a6de"/>
    <path d="M306 156 A153 153 0 0 1 156 306 V228 A75 75 0 0 0 228 156 Z" fill="#d0112b"/>
    <path d="M150 306 A153 153 0 0 1 0 156 H78 A75 75 0 0 0 150 228 Z" fill="#8dc63f"/>
    <circle cx="153" cy="153" r="30" fill="#e9eef2"/>
    <g fill="none" stroke="#fff" stroke-width="2.5">
      <rect x="68" y="58" width="30" height="22" rx="2"/><path d="M76 88h14M83 80v8"/>
      <rect x="210" y="58" width="30" height="22" rx="2"/><circle cx="225" cy="69" r="5"/>
      <circle cx="225" cy="240" r="14"/><path d="M225 222v6M225 252v6M207 240h6M237 240h6"/>
      <circle cx="83" cy="225" r="8"/><path d="M68 252c0-10 7-16 15-16s15 6 15 16"/>
    </g>
  </svg>
  <div class="partners"><div class="partner"><span class="dot"></span>Quiet Harbor</div><div class="partner k7"><span class="dot"></span>k7gridworks</div></div>
  <div class="page-no">Page No:04</div>
</section>

<section class="slide s5">
  <div class="backdrop" role="img" aria-label="Faint network connection background"></div>
  <div class="title-band">Analysis</div>
  <div class="brand brand-top"><span class="dot"></span>VeroTide</div>
  <p class="analysis-text">Sed ut perspiciatis unde omnis iste natus error sit voluptatem accusantium doloremque laudantium, totam rem aperiam, eaque ipsa quae ab illo inventore veritatis et quasi architecto beatae vitae dicta sunt explicabo. Nemo enim ipsam voluptatem quia voluptas sit aspernatur aut odit aut fugit, sed quia consequuntur magni dolores eos qui ratione voluptatem sequi nesciunt. Neque porro quisquam est, qui dolorem ipsum quia dolor sit amet, consectetur, adipisci velit, sed quia non numquam eius modi tempora incidunt ut labore et dolore magnam aliquam quaerat voluptatem. Ut enim ad minima veniam, quis nostrum exercitationem ullam corporis</p>
  <ul class="bars">
    <li><span class="fill" style="width:56%"></span><span class="pct">60%</span></li>
    <li class="red"><span class="fill" style="width:70%"></span><span class="pct">80%</span></li>
    <li><span class="fill" style="width:42%"></span><span class="pct">40%</span></li>
    <li class="red"><span class="fill" style="width:32%"></span><span class="pct">30%</span></li>
    <li><span class="fill" style="width:65%"></span><span class="pct">70%</span></li>
    <li class="red"><span class="fill" style="width:54%"></span><span class="pct">60%</span></li>
  </ul>
  <div class="partners"><div class="partner"><span class="dot"></span>Quiet Harbor</div><div class="partner k7"><span class="dot"></span>k7gridworks</div></div>
  <div class="page-no">Page No:05</div>
</section>

<section class="slide s6">
  <div class="backdrop" role="img" aria-label="Faint router and keyboard background photo"></div>
  <div class="brand"><span class="dot"></span>VeroTide</div>
  <h2 class="thanks">Thank you</h2>
  <div class="contact c1">
    <div class="icon"><svg width="22" height="26" viewBox="0 0 22 26"><path d="M11 1C5.5 1 2 5 2 10c0 6 9 15 9 15s9-9 9-15c0-5-3.5-9-9-9z" fill="#fff"/><circle cx="11" cy="10" r="3.5" fill="#006b3a"/></svg></div>
    <div><strong>Address :</strong><span>174 , Lorem Ipsum Dolor Sit</span></div>
  </div>
  <div class="contact c2">
    <div class="icon"><svg width="24" height="18" viewBox="0 0 24 18"><rect x="1" y="1" width="22" height="16" rx="2" fill="#fff"/><path d="M2 2l10 8 10-8" fill="none" stroke="#006b3a" stroke-width="2"/></svg></div>
    <div><strong>Email:</strong><span>info@verotide.com.au</span></div>
  </div>
  <div class="contact c3">
    <div class="icon"><svg width="22" height="22" viewBox="0 0 22 22"><path d="M5 1l4 5-2.5 2.5c1.5 3 4 5.5 7 7L16 13l5 4-2 4C10 21 1 12 1 3z" fill="#fff"/></svg></div>
    <div><strong>Phone :</strong><span>+1 555 010 0188</span></div>
  </div>
  <div class="partners"><div class="partner"><span class="dot"></span>Quiet Harbor</div><div class="partner k7"><span class="dot"></span>k7gridworks</div></div>
  <div class="page-no">Page No:06</div>
</section>

</body>
</html>
```